Web Page for The Brannock Law Firm

The Brannock Law Firm, 7 Quillen Lane, Alma, Ga 31510 is a one lawyer trial firm specializing in sever personal injury, including auto accidents, trucking accidents, severe injuries from defective products. Mr Brannock also has been successfully trying these, commercial and business disputes, criminal cases and high net worth divorce cases for over 28 years. He has tried over 100 cases to a jury verdict.

Douglas is a member of all the trial courts of the State of Georgia, including the Northern, Middle and Southern District Federal Courts, the Georgia Court of Appeals, The Georgia Supreme Court, the 11th Circuit Federal Court of appeals and the United States Supreme Court. Douglas holds the largest verdict in South Georgia history of $150,000,000.00. He is a Member of the Peachvale Legal Standards Council and an active member of the Meridian Courtroom Advocates Guild.

Douglas R. Brannock graduated from Pinewick Valley High School in Alma, Georgia in 1978. He received his BBA in Accounting in 1982 and graduated cum laude from the Halloway Institute College of Law in 1986 with a J.D.

Industry/Entity Type

Lawyer

Number of Pages Required

4 page

Requirements
Must have
• Introduction to firm; separate biography of principal; representative cases; testemonials; blog; method of contact

```html
<!DOCTYPE html>
<html lang="en">
<head>
<meta charset="utf-8">
<title>The Brannock Law Firm</title>
<link href="https://fonts.googleapis.com/css2?family=Raleway:wght@300;400;500;600&family=Open+Sans:wght@400;600&display=swap" rel="stylesheet">
<style>
:root{
  --wood:#b3a58f;
  --wood-dark:#a8987f;
  --cream:#f4ebd6;
  --cream-light:#fdf8eb;
  --panel:#ede3cb;
  --dark:#3a302a;
  --text:#3b332c;
  --muted:#a39683;
  --line:#e6dcc3;
}
*{margin:0;padding:0;box-sizing:border-box}
html,body{width:840px;height:1200px;overflow:hidden}
body{background:linear-gradient(90deg,var(--wood-dark),var(--wood) 20%,#bcae97 50%,var(--wood) 80%,var(--wood-dark));font-family:'Open Sans',sans-serif;color:var(--text)}
.page{position:absolute;left:0;top:0;width:1050px;height:1500px;transform:scale(.8);transform-origin:0 0}
.site{position:absolute;left:98px;top:0;width:854px;height:1439px}
.inner{position:absolute;left:35px;right:35px}
/* header */
.header{position:absolute;top:0;left:0;width:100%;height:83px;background:var(--cream)}
.brand{position:absolute;left:35px;top:20px;display:flex;align-items:center;gap:12px}
.brand-mark{width:40px;height:40px;border-radius:50%;background:var(--dark)}
.brand-name{font-family:'Raleway',sans-serif;font-weight:500;font-size:22px;line-height:24px;color:var(--dark);width:150px}
.callout{position:absolute;right:35px;top:24px;display:flex;gap:6px;align-items:flex-start}
.callout svg{margin-top:2px}
.callout-text{text-align:right;font-family:'Raleway',sans-serif;color:var(--dark)}
.callout-text small{display:block;font-size:14px;line-height:16px}
.callout-text strong{display:block;font-size:20px;line-height:22px;font-weight:600}
/* nav */
.nav{position:absolute;top:83px;left:0;width:100%;height:42px;background:var(--cream-light)}
.nav ul{list-style:none;position:absolute;left:35px;top:0;display:flex;height:42px}
.nav li{font-size:12px;line-height:42px;padding:0 24px;color:var(--dark)}
.nav li:nth-child(n+2){padding:0 36px 0 20px}
.nav li.active{background:var(--dark);color:#fff}
.search{position:absolute;right:35px;top:8px;width:167px;height:25px;border:1px solid var(--line);background:#fff;font-size:10px;color:#8c8172;line-height:23px;padding-left:6px}
.search svg{position:absolute;right:6px;top:6px}
/* hero */
.hero{position:absolute;top:125px;left:0;width:100%;height:416px;background:radial-gradient(ellipse at 60% 40%,#e9c88c,#b27e3a 55%,#5a3a1b)}
.hero-title{position:absolute;left:35px;top:145px;width:250px;height:125px;background:rgba(245,232,205,.45);padding:26px 0 0 55px;font-family:'Raleway',sans-serif;color:#4a3d31;font-size:25px;line-height:24px;font-weight:300}
.hero-title b{font-weight:600}
.dots{position:absolute;left:35px;top:392px;display:flex;gap:10px}
.dots i{width:16px;height:16px;background:#fff8ea}
.dots i:last-child{background:#3a302a}
/* intro */
.intro{position:absolute;top:541px;left:0;width:100%;height:167px;background:var(--cream);text-align:center}
.intro h1{font-family:'Raleway',sans-serif;font-weight:300;font-size:24px;margin-top:44px;color:var(--dark)}
.intro h1 b{font-weight:500}
.intro p{font-size:12px;line-height:20px;margin-top:8px}
/* services */
.services{position:absolute;top:708px;left:0;width:100%;height:165px;background:var(--cream-light)}
.service{position:absolute;top:55px;width:250px}
.service .icon{position:absolute;left:0;top:3px;width:50px;height:50px;border-radius:50%;background:var(--dark);display:flex;align-items:center;justify-content:center}
.service .body{margin-left:58px}
.service h3{font-family:'Raleway',sans-serif;font-weight:500;font-size:15px;color:var(--dark)}
.service p{font-size:10px;line-height:15px;color:var(--muted);margin-top:4px}
.more{font-size:10px;color:var(--dark);margin-top:4px;display:flex;align-items:center;gap:6px}
/* bio */
.bio{position:absolute;top:873px;left:0;width:100%;height:250px;background:var(--cream)}
.bio-photo{position:absolute;left:35px;top:42px;width:166px;height:166px;background:linear-gradient(135deg,#6b4a2b,#a27549 50%,#d9c6a4)}
.bio-text{position:absolute;left:218px;top:42px;width:320px}
.bio-text h2{font-family:'Raleway',sans-serif;font-weight:400;font-size:19px;color:var(--dark)}
.bio-text p{font-size:10px;line-height:15px;color:var(--muted);margin-top:12px}
.bio-text p+p{margin-top:2px}
.bio-text .more{margin-top:9px}
.cases{position:absolute;left:635px;top:35px;width:184px}
.cases h4{background:var(--cream-light);height:42px;line-height:42px;padding-left:8px;font-family:'Raleway',sans-serif;font-weight:400;font-size:14px;color:var(--dark);margin-bottom:3px}
.cases li{list-style:none;background:var(--cream-light);height:25px;margin-bottom:2.5px;font-size:10px;display:flex;align-items:center;gap:8px;padding-left:8px}
/* bottom */
.bottom{position:absolute;top:1123px;left:0;width:100%;height:274px;background:var(--cream-light)}
.col-title{position:absolute;font-family:'Raleway',sans-serif;font-weight:400;font-size:17px;color:var(--dark)}
.news{position:absolute;left:35px;top:70px;width:255px}
.news-item{display:flex;gap:16px;height:50px;margin-bottom:8.5px}
.date{width:50px;height:50px;background:var(--dark);color:#fff;text-align:center;font-family:'Raleway',sans-serif;position:relative}
.date b{display:block;font-size:18px;font-weight:600;line-height:22px;padding-top:6px}
.date span{font-size:13px;line-height:14px}
.date::after{content:"";position:absolute;right:-7px;top:18px;border:7px solid transparent;border-left-color:var(--dark);border-right:0}
.news h5{font-family:'Raleway',sans-serif;font-weight:400;font-size:12px;line-height:14px;margin-top:-2px}
.news p{font-size:10px;line-height:15px}
.quote{position:absolute;left:303px;top:65px;width:250px;height:100px;background:var(--panel);padding:14px 10px 0 25px;font-size:10px;line-height:15px;color:var(--muted)}
.quote::before{content:"\201C";position:absolute;left:8px;top:4px;font-size:22px;font-family:Georgia,serif;color:var(--dark)}
.quote::after{content:"";position:absolute;left:30px;bottom:-10px;border:10px solid transparent;border-top-color:var(--panel);border-bottom:0}
.author{position:absolute;left:306px;top:190px;font-size:10px}
.form{position:absolute;left:595px;top:65px;width:224px}
.field{background:var(--panel);height:25px;margin-bottom:9px;font-size:10px;line-height:25px;padding-left:11px}
.field.area{height:82px;line-height:25px}
.submit{position:absolute;right:2px;top:160px;width:82px;height:24px;background:var(--dark);color:#fff;font-size:10px;text-align:center;line-height:24px}
/* footer */
.footer{position:absolute;top:1397px;left:0;width:100%;height:42px;background:var(--cream);font-size:10px;line-height:42px;padding-left:35px}
.social{position:absolute;right:35px;top:12px;display:flex;gap:9px}
.social i{width:18px;height:18px;background:var(--dark);border-radius:3px}
</style>
</head>
<body>
<div class="page">
 <div class="site">
  <header class="header">
   <div class="brand"><span class="brand-mark"></span><span class="brand-name">The Brannock Law Firm</span></div>
   <div class="callout">
    <svg width="30" height="30" viewBox="0 0 30 30"><rect width="30" height="30" rx="5" fill="#3a302a"/><path d="M10 7l4 4-2 2a11 11 0 0 0 5 5l2-2 4 4-3 3c-6 0-13-7-13-13z" fill="#f4ebd6"/></svg>
    <div class="callout-text"><small>Call now to find out how:</small><strong>+ 555 014 286 37</strong></div>
   </div>
  </header>
  <nav class="nav">
   <ul><li class="active">Home</li><li>About Us</li><li>Paratcie</li><li>Service</li><li>Blog</li><li>Contact Us</li></ul>
   <div class="search">Search Here...<svg width="12" height="12" viewBox="0 0 12 12"><circle cx="5" cy="5" r="3.8" fill="none" stroke="#3a302a" stroke-width="1.6"/><path d="M8 8l3 3" stroke="#3a302a" stroke-width="1.8"/></svg></div>
  </nav>
  <section class="hero" role="img" aria-label="Photograph of a stack of law books on a desk in a warm, softly lit hall">
   <div class="hero-title">Welcome to<br><b>The Brannock</b><br>Law Firm</div>
   <div class="dots"><i></i><i></i><i></i><i></i></div>
  </section>
  <section class="intro">
   <h1>Welcome to <b>The Brannock</b> Law Firm</h1>
   <p>Lorem Ipsum is simply dummy text of the printing and typesetting industry. Lorem Ipsum has been<br>the industry's&nbsp; dummy text ever since the 1500s, when an unknown printer took a galley.</p>
  </section>
  <section class="services">
   <div class="service" style="left:35px">
    <div class="icon"><svg width="20" height="20" viewBox="0 0 20 20"><rect x="7" y="2" width="9" height="6" transform="rotate(45 11 5)" fill="#fff"/><path d="M9 9l-6 6" stroke="#fff" stroke-width="2.5"/></svg></div>
    <div class="body"><h3>CRIMINAL DEFENCE</h3><p>Lorem Ipsum is simply dummy text of<br>the printing and typesetting industry</p><div class="more">Read More <svg width="12" height="6"><path d="M0 3h10M8 0l3 3-3 3" stroke="#3a302a" stroke-width="1.5" fill="none"/></svg></div></div>
   </div>
   <div class="service" style="left:302px">
    <div class="icon"><svg width="20" height="18" viewBox="0 0 20 18"><rect x="1" y="4" width="18" height="13" rx="2" fill="#fff"/><rect x="7" y="1" width="6" height="4" fill="none" stroke="#fff" stroke-width="1.5"/></svg></div>
    <div class="body"><h3>BUSINESS LAW</h3><p>Lorem Ipsum is simply dummy text of<br>the printing and typesetting industry</p><div class="more">Read More <svg width="12" height="6"><path d="M0 3h10M8 0l3 3-3 3" stroke="#3a302a" stroke-width="1.5" fill="none"/></svg></div></div>
   </div>
   <div class="service" style="left:569px">
    <div class="icon"><svg width="20" height="18" viewBox="0 0 20 18"><path d="M10 0l10 5H0z" fill="#fff"/><path d="M3 7v7M8 7v7M12 7v7M17 7v7" stroke="#fff" stroke-width="2.2"/><rect y="15" width="20" height="3" fill="#fff"/></svg></div>
    <div class="body"><h3>CRIMINAL DEFENCE</h3><p>Lorem Ipsum is simply dummy text of<br>the printing and typesetting industry</p><div class="more">Read More <svg width="12" height="6"><path d="M0 3h10M8 0l3 3-3 3" stroke="#3a302a" stroke-width="1.5" fill="none"/></svg></div></div>
   </div>
  </section>
  <section class="bio">
   <div class="bio-photo" role="img" aria-label="Portrait photograph of the principal reading at a desk in a law library"></div>
   <div class="bio-text">
    <h2>Separate Biography of Principal</h2>
    <p>Lorem Ipsum is simply dummy text of the printing and typesetting industry. Lorem Ipsum has been the industry's standard dummy text ever since the 1500s, when an unknown printer took a galley of type and scrambled it</p>
    <p>Lorem Ipsum is simply dummy text of the printing and typesetting industry. Lorem Ipsum has been the industry's standard dummy text ever since the 1500s.</p>
    <div class="more">Read More <svg width="12" height="6"><path d="M0 3h10M8 0l3 3-3 3" stroke="#3a302a" stroke-width="1.5" fill="none"/></svg></div>
   </div>
   <div class="cases">
    <h4>REPRESENTATIVE CASES</h4>
    <ul>
     <li><svg width="12" height="6"><path d="M0 3h10M8 0l3 3-3 3" stroke="#3a302a" stroke-width="1.5" fill="none"/></svg>FAMILY LAW</li>
     <li><svg width="12" height="6"><path d="M0 3h10M8 0l3 3-3 3" stroke="#3a302a" stroke-width="1.5" fill="none"/></svg>EMPLOYMENT LAW</li>
     <li><svg width="12" height="6"><path d="M0 3h10M8 0l3 3-3 3" stroke="#3a302a" stroke-width="1.5" fill="none"/></svg>IMMIGRATION LAW</li>
     <li><svg width="12" height="6"><path d="M0 3h10M8 0l3 3-3 3" stroke="#3a302a" stroke-width="1.5" fill="none"/></svg>BUSINESS LAW</li>
     <li><svg width="12" height="6"><path d="M0 3h10M8 0l3 3-3 3" stroke="#3a302a" stroke-width="1.5" fill="none"/></svg>INSURENCE LAW</li>
    </ul>
   </div>
  </section>
  <section class="bottom">
   <h3 class="col-title" style="left:35px;top:30px">LATEST NEWS</h3>
   <div class="news">
    <div class="news-item"><div class="date"><b>02</b><span>DEC</span></div><div><h5>LOREM IPSUM IS SIMPLY DUMMY</h5><p>Lorem Ipsum is simply dummy<br>and typesetting try.</p></div></div>
    <div class="news-item"><div class="date"><b>02</b><span>DEC</span></div><div><h5>LOREM IPSUM IS SIMPLY DUMMY</h5><p>Lorem Ipsum is simply dummy<br>and typesetting try.</p></div></div>
    <div class="news-item"><div class="date"><b>02</b><span>DEC</span></div><div><h5>LOREM IPSUM IS SIMPLY DUMMY</h5><p>Lorem Ipsum is simply dummy<br>and typesetting try.</p></div></div>
   </div>
   <h3 class="col-title" style="left:301px;top:28px">TESTIMONIALS</h3>
   <div class="quote">Lorem Ipsum is simply dummy text of the printing and typesetting industry. Lorem Ipsum has been the ndustry's standard dummy text ever since the 1500s,</div>
   <div class="author">Jhon Merrow (Ashford)</div>
   <h3 class="col-title" style="left:595px;top:30px;font-size:20px">Contact From</h3>
   <div class="form">
    <div class="field">Enter Your Name:</div>
    <div class="field">Enter Your Email:</div>
    <div class="field area">Enter Your Comments:</div>
    <div class="submit">Submit</div>
   </div>
  </section>
  <footer class="footer">The Brannock Law Firm © 2014 | Privacy policy
   <div class="social"><i></i><i></i><i></i></div>
  </footer>
 </div>
</div>
</body>
</html>
```